MIRA TOLLEN'S Gingerbeer beverages needs a logo design for a our label.

Mira Tollen is the name of my ginger beer. the font I would like use for MIRA TOLLEN is Emperator hand Ess and a script for Ginger beer. the label will be printed on clear vinyl. Its a Extra Spicy from 700 year old recipe. We make it with a wild probiotic. The finial design should create a thirst for great tasting product have a simple image that reflect nature of the ginger planet. Colors can be bright red like maroon and gold. Business is in Texas.

```html
<!DOCTYPE html>
<html lang="en">
<head>
<meta charset="utf-8">
<title>Mira Tollen Ginger Beer – Label</title>
<link rel="stylesheet" href="https://fonts.googleapis.com/css2?family=Marcellus&family=Yellowtail&family=Damion&family=Oswald:wght@500&family=Josefin+Sans:wght@600&display=block">
<style>
  :root {
    --backdrop: #7a7a7a;
    --label-red: #b01118;
    --gold-light: #e6d35a;
    --gold-mid: #c49a2c;
    --gold-dark: #8c6420;
    --ink-white: #ffffff;
    --accent-gold: #e5c572;
    --ginger-tone: #e3c57a;
    --ginger-edge: #6e0a0c;
  }
  html, body {
    margin: 0;
    padding: 0;
    width: 800px;
    height: 1200px;
    overflow: hidden;
    background: var(--backdrop);
  }
  .canvas {
    width: 800px;
    height: 1200px;
    display: block;
  }
  .label-tagline {
    font-family: "Josefin Sans", sans-serif;
    font-weight: 600;
    font-size: 20px;
    letter-spacing: 7px;
    fill: var(--accent-gold);
  }
  .label-name {
    font-family: "Marcellus", serif;
    font-size: 130px;
    fill: var(--ink-white);
  }
  .label-style {
    font-family: "Yellowtail", "Damion", cursive;
    font-size: 66px;
    fill: var(--accent-gold);
  }
  .label-volume {
    font-family: "Oswald", sans-serif;
    font-weight: 500;
    font-size: 44px;
    fill: var(--ink-white);
  }
</style>
</head>
<body>
<svg class="canvas" viewBox="0 0 800 1200" xmlns="http://www.w3.org/2000/svg">
  <defs>
    <linearGradient id="gold-ring" x1="0" y1="0" x2="1" y2="1">
      <stop offset="0" stop-color="#8c6420"/>
      <stop offset="0.3" stop-color="#e6d35a"/>
      <stop offset="0.55" stop-color="#8c6420"/>
      <stop offset="0.8" stop-color="#c49a2c"/>
      <stop offset="1" stop-color="#e6d35a"/>
    </linearGradient>
    <path id="tagline-arc" d="M150,600 A250,370 0 0 1 650,600"/>
  </defs>

  <g class="label">
    <ellipse class="label-ring-gold" cx="400" cy="600" rx="330" ry="450" fill="url(#gold-ring)"/>
    <ellipse class="label-ring-white" cx="400" cy="600" rx="310" ry="430" fill="var(--ink-white)"/>
    <ellipse class="label-ring-inner-gold" cx="400" cy="600" rx="296" ry="416" fill="url(#gold-ring)"/>
    <ellipse class="label-field" cx="400" cy="600" rx="290" ry="410" fill="var(--label-red)"/>

    <text class="label-tagline">
      <textPath href="#tagline-arc" startOffset="50%" text-anchor="middle">WILD PROBIOTIC · EXTRA SPICY</textPath>
    </text>

    <text class="label-name" x="400" y="505" text-anchor="middle" textLength="370" lengthAdjust="spacingAndGlyphs">MIRA</text>
    <text class="label-name" x="400" y="650" text-anchor="middle" textLength="500" lengthAdjust="spacingAndGlyphs">TOLLEN</text>

    <text class="label-style" x="325" y="790" text-anchor="end">Ginger</text>
    <ellipse class="ginger-root" role="img" aria-label="Engraved illustration of a ginger root" cx="405" cy="770" rx="62" ry="52" fill="var(--ginger-tone)" stroke="var(--ginger-edge)" stroke-width="4"/>
    <text class="label-style" x="485" y="790" text-anchor="start">Beer</text>

    <rect class="wheat-sprig wheat-left" role="img" aria-label="Gold wheat sprig ornament" x="250" y="850" width="75" height="70" rx="26" fill="var(--accent-gold)" transform="rotate(-35 287 885)"/>
    <rect class="wheat-sprig wheat-right" role="img" aria-label="Gold wheat sprig ornament" x="475" y="850" width="75" height="70" rx="26" fill="var(--accent-gold)" transform="rotate(35 512 885)"/>

    <text class="label-volume" x="400" y="912" text-anchor="middle">32 fl oz</text>
  </g>
</svg>
</body>
</html>
```